Business Card Design

We would like a business card that utilizes our current logo and keeps with the same feel - elegant and organic. Our farm isn't about mass production, it's about excellence, education, beautiful events and flowers - people, culture, and community.

Target Market(s)

Patrons to our farm who are interested in weddings, events, or our flowers and vegetables.

Contact Information for Business Card

Name, address, cell email (Danielle Hoskins, 2716 Wrenfield Rd, Larkmoor, CO 80599, cell 30.412.6638, email danielle@wrenfieldacres.com)

```html
<!DOCTYPE html>
<html lang="en">
<head>
<meta charset="utf-8">
<title>Wrenfield Acres — Business Card</title>
<link rel="stylesheet" href="https://fonts.googleapis.com/css2?family=Inter:wght@400;700&display=swap">
<style>
  :root {
    --backdrop: #2a2a2a;
    --card-white: #ffffff;
    --sage: #748a74;
    --sage-deep: #5d745f;
    --sage-name: #647a66;
    --bronze: #9c7646;
    --ink: #4e4e4e;
  }
  * { box-sizing: border-box; margin: 0; padding: 0; }
  html, body {
    width: 1200px; height: 1108px; overflow: hidden;
    background: var(--backdrop);
    font-family: "Inter", sans-serif;
  }
  .stage {
    position: relative; width: 1200px; height: 1108px;
    display: flex; justify-content: center; align-items: center; gap: 60px;
  }
  .card {
    width: 400px; height: 700px; border-radius: 28px;
    display: flex; flex-direction: column; align-items: center;
  }
  .card--front { background: var(--card-white); padding-top: 120px; }
  .card--back { background: var(--sage); justify-content: center; }

  .brand-name {
    font-weight: 400; font-size: 38px; color: var(--sage);
    letter-spacing: 0.5px; text-align: center; line-height: 1.1;
  }
  .card--back .brand-name { color: var(--sage-deep); font-size: 42px; }

  .person-name {
    margin-top: 90px; font-weight: 700; font-size: 25px;
    color: var(--sage-name); letter-spacing: 0.5px; text-transform: uppercase;
  }

  .icon-row {
    margin-top: 80px; display: flex; align-items: center; gap: 8px;
  }
  .rule { display: block; height: 2px; background: var(--bronze); }
  .icon-row .rule { width: 52px; }
  .icon-tile {
    width: 26px; height: 26px; border-radius: 5px; background: var(--bronze);
    display: flex; align-items: center; justify-content: center;
  }
  .icon-tile svg { width: 16px; height: 16px; }

  .contact-list {
    list-style: none; margin-top: 14px; text-align: center;
    color: var(--ink); font-size: 17px; line-height: 1.55;
  }
  .divider { width: 110px; margin-top: 30px; }
  .address {
    margin-top: 28px; text-align: center; font-style: normal;
    color: var(--ink); font-size: 17px; line-height: 1.55;
  }
</style>
</head>
<body>
<main class="stage">
  <section class="card card--front">
    <p class="brand-name">Wrenfield Acres</p>
    <h1 class="person-name">Danielle Hoskins</h1>

    <div class="icon-row">
      <span class="rule"></span>
      <span class="icon-tile" aria-label="Phone">
        <svg viewBox="0 0 16 16" fill="none" stroke="#fff" stroke-width="1.5" stroke-linecap="round" stroke-linejoin="round">
          <path d="M4 2.5l2 .3.8 2.6-1.3 1.1a8 8 0 0 0 4 4l1.1-1.3 2.6.8.3 2a1.5 1.5 0 0 1-1.5 1.5A10.5 10.5 0 0 1 2.5 4 1.5 1.5 0 0 1 4 2.5z"/>
        </svg>
      </span>
      <span class="icon-tile" aria-label="Email">
        <svg viewBox="0 0 16 16" fill="none" stroke="#fff" stroke-width="1.5" stroke-linejoin="round">
          <rect x="2" y="4" width="12" height="8.5" rx="1"/>
          <path d="M2.5 4.5L8 9l5.5-4.5"/>
        </svg>
      </span>
      <span class="icon-tile" aria-label="Website">
        <svg viewBox="0 0 16 16" fill="none" stroke="#fff" stroke-width="1.4">
          <circle cx="8" cy="8" r="5.8"/>
          <ellipse cx="8" cy="8" rx="2.4" ry="5.8"/>
          <path d="M2.2 8h11.6"/>
        </svg>
      </span>
      <span class="rule"></span>
    </div>

    <ul class="contact-list">
      <li>30.412.6638</li>
      <li>danielle@wrenfieldacres.com</li>
      <li>www.wrenfieldacres.com</li>
    </ul>

    <span class="rule divider"></span>

    <address class="address">
      2716 Wrenfield Rd<br>
      Larkmoor, CO 80599
    </address>
  </section>

  <section class="card card--back">
    <p class="brand-name">Wrenfield Acres</p>
  </section>
</main>
</body>
</html>
```